Pelvorin iOS and Android mobile app design

Astronomical Dawn
The time at which the sun is 18 degrees below the horizon in the morning. Astronomical dawn is that point in time at which the sun starts lightening the sky. Prior to this time during the morning, the sky is completely dark.

My app will alert users and allow them to set reminders and alarms to when astronomical dawn starts and ends, when actual sunrise happens.

I would like something that allows the user to pick a date .. maybe show a scrollable current week to tap and see what time this even begins and ends .. then when it starts I want a countdown to sunrise graphic animation that shows until sunrise ...

Requirements
Must have
• Simplicity and elegance, Figma
Nice to have
• Material design and icons
Should not have
• Graphics that cost money

```html
<!DOCTYPE html>
<html lang="en">
<head>
<meta charset="utf-8">
<title>Pelvorin – app screens</title>
<link rel="stylesheet" href="https://fonts.googleapis.com/css2?family=EB+Garamond:wght@400;500&family=Roboto:wght@300;400;500;700&display=swap">
<style>
:root{
  --stage:#000;
  --orange:#e98c1f;
  --plum:#2e1a5c;
  --header-a:#2f1a4e;
  --header-b:#4a1f55;
  --navy:#282a72;
  --sky-blue:#a4c7e9;
  --ink:#1c1c1c;
  --white:#fff;
}
*{box-sizing:border-box;margin:0;padding:0}
html,body{width:760px;height:1200px;overflow:hidden;background:var(--stage)}
body{position:relative;font-family:"Roboto",sans-serif}
.screen{position:absolute;overflow:hidden}
.abs{position:absolute}

/* login */
.login{background:
  radial-gradient(circle at 80% 8%,rgba(80,210,235,.75),transparent 40%),
  radial-gradient(circle at 15% 10%,rgba(100,185,215,.7),transparent 45%),
  linear-gradient(180deg,#72c6df 0%,#b4d6df 30%,#dfe3d6 50%,#f8eee4 66%,#f0c7b8 82%,#e6aa9c 100%)}
.login-bg{position:absolute;inset:0}
.brand-title{font-family:"EB Garamond",serif;font-weight:400;color:#111;text-align:center;width:100%;letter-spacing:.02em}
.cartouche{position:absolute;background:rgba(235,240,235,.55);border-radius:38px}
.field{position:absolute;background:var(--white);border-radius:999px;display:flex;align-items:center;justify-content:space-between;color:#444;font-weight:300}
.field svg{display:block}
.signin{position:absolute;background:var(--orange);border-radius:14px;color:var(--white);display:flex;align-items:center;justify-content:space-between}
.or-badge{position:absolute;border-radius:50%;background:var(--white);display:flex;align-items:center;justify-content:center;color:#666;font-weight:300}
.no-account{position:absolute;width:100%;text-align:center;color:#222;font-weight:300}
.register{position:absolute;background:var(--plum);color:var(--white);border-radius:10px;display:flex;align-items:center;justify-content:center;box-shadow:0 2px 3px rgba(0,0,0,.25)}
.system-nav{position:absolute;left:0;width:100%;display:flex;justify-content:space-around;padding:0 26px}

/* app header */
.app-header{position:absolute;left:0;top:0;width:100%;height:36px;background:linear-gradient(90deg,var(--header-a),var(--header-b));display:flex;align-items:center;justify-content:space-between;padding:0 12px 0 17px;z-index:2}
.app-header .name{font-family:"EB Garamond",serif;color:var(--white);font-size:13.5px;letter-spacing:.04em}

/* planner */
.night-sky{position:absolute;left:0;top:36px;width:100%;height:300px;background:linear-gradient(180deg,#15151c 0%,#1e1e28 55%,#34323f 100%)}
.section-label{position:absolute;left:0;width:100%;display:flex;align-items:center;justify-content:center;gap:12px;color:var(--white);font-weight:500;font-size:13px;letter-spacing:.06em}
.section-label::before,.section-label::after{content:"";width:57px;height:1px;background:#ddd}
.select{position:absolute;height:33px;background:var(--white);border-radius:17px;box-shadow:0 5px 0 #3c1f5c;display:flex;align-items:center;justify-content:space-between;padding:0 9px 0 12px;font-size:11.5px;color:var(--ink)}
.time-pill{position:absolute;left:30px;width:214px;height:41px;border:1px solid #c9d7f0;border-radius:21px;overflow:hidden;display:flex;align-items:center}
.time-pill .label{flex:1;display:flex;align-items:center;gap:12px;padding-left:14px;color:var(--white);font-size:11px;letter-spacing:.03em}
.time-pill .value{width:92px;height:100%;background:var(--sky-blue);border-radius:20px 0 0 20px;display:flex;align-items:center;justify-content:center;color:var(--navy);font-size:13px;font-weight:500;letter-spacing:.03em}
.reminder-bar{position:absolute;left:0;top:449px;width:100%;height:49px;background:var(--orange);display:flex;align-items:center;justify-content:center;gap:12px;color:var(--white);font-weight:700;font-size:13px;letter-spacing:.04em}

/* countdown */
.sunrise-scene{position:absolute;inset:0;background:linear-gradient(180deg,#5f5448 0%,#6b5a44 30%,#8a6534 52%,#a8691f 66%,#6a4318 80%,#1d1611 100%)}
.greeting{position:absolute;left:104px;top:82px;width:75px;height:30px;background:var(--sky-blue);border-radius:9px;display:flex;align-items:center;justify-content:center;font-family:"EB Garamond",serif;font-size:13px;color:#1d2338}
.headline{position:absolute;left:0;top:134px;width:100%;text-align:center;font-family:"EB Garamond",serif;font-weight:400;color:#f6f1ea;font-size:21px;line-height:31px;letter-spacing:.01em;text-shadow:0 2px 3px rgba(0,0,0,.45)}
.flip{position:absolute;top:232px;display:flex;gap:1px}
.flip span{width:26px;height:40px;background:linear-gradient(180deg,#2a2a2a 0 49%,#111 50% 100%);color:#f3ece2;font-family:"Roboto",sans-serif;font-weight:300;font-size:33px;display:flex;align-items:center;justify-content:center;border-bottom:2px solid #888}
.unit{position:absolute;top:284px;width:60px;text-align:center;font-family:"EB Garamond",serif;color:#f1e6d6;font-size:9.5px;letter-spacing:.02em}
</style>
</head>
<body>

<!-- compact sign-in -->
<section class="screen login" style="left:103px;top:77px;width:217px;height:468px;border-radius:18px">
  <div class="login-bg" role="img" aria-label="Soft blurred bokeh backdrop in cyan, cream and rose tones"></div>
  <h1 class="brand-title abs" style="top:50px;font-size:16px">PELVORIN</h1>
  <div class="cartouche" style="left:10px;top:105px;width:204px;height:120px"></div>
  <div class="field" style="left:30px;top:133px;width:160px;height:26px;padding:0 10px;font-size:7.5px">Username
    <svg width="11" height="11" viewBox="0 0 24 24" fill="none" stroke="#222" stroke-width="1.8"><circle cx="12" cy="12" r="10"/><circle cx="12" cy="10" r="3.5"/><path d="M5.5 19c2-3 4-4 6.5-4s4.5 1 6.5 4"/></svg></div>
  <div class="field" style="left:30px;top:166px;width:160px;height:26px;padding:0 10px;font-size:7.5px">Password
    <svg width="10" height="11" viewBox="0 0 24 24" fill="none" stroke="#222" stroke-width="1.8"><rect x="5" y="10" width="14" height="12" rx="2"/><path d="M8 10V7a4 4 0 0 1 8 0v3"/><circle cx="12" cy="16" r="1.3"/></svg></div>
  <div class="signin" style="left:28px;top:246px;width:160px;height:30px;padding:0 14px;font-size:14px">Sign In
    <svg width="22" height="10" viewBox="0 0 44 20" fill="none" stroke="#fff" stroke-width="2"><path d="M0 10h42M33 2l9 8-9 8"/></svg></div>
  <div class="or-badge" style="left:95px;top:312px;width:26px;height:26px;font-size:7px">OR</div>
  <p class="no-account" style="top:360px;font-size:10px">Don't have a Pelvorin Account</p>
  <div class="register" style="left:83px;top:391px;width:53px;height:21px;font-size:7px">Register</div>
  <div class="system-nav" style="top:437px">
    <svg width="13" height="14" viewBox="0 0 26 28" fill="none" stroke="#111" stroke-width="2.5"><path d="M22 3L4 14l18 11z"/></svg>
    <svg width="14" height="14" viewBox="0 0 28 28" fill="none" stroke="#111" stroke-width="2.5"><circle cx="14" cy="14" r="11"/></svg>
    <svg width="12" height="12" viewBox="0 0 24 24" fill="none" stroke="#111" stroke-width="2.8"><rect x="2" y="2" width="20" height="20"/></svg>
  </div>
</section>

<!-- full sign-in -->
<section class="screen login" style="left:410px;top:77px;width:279px;height:496px">
  <div class="login-bg" role="img" aria-label="Soft blurred bokeh backdrop in cyan, cream and rose tones"></div>
  <h1 class="brand-title abs" style="top:30px;font-size:21px">PELVORIN</h1>
  <div class="cartouche" style="left:20px;top:93px;width:248px;height:150px"></div>
  <div class="field" style="left:43px;top:130px;width:194px;height:31px;padding:0 12px;font-size:9px">Username
    <svg width="13" height="13" viewBox="0 0 24 24" fill="none" stroke="#222" stroke-width="1.8"><circle cx="12" cy="12" r="10"/><circle cx="12" cy="10" r="3.5"/><path d="M5.5 19c2-3 4-4 6.5-4s4.5 1 6.5 4"/></svg></div>
  <div class="field" style="left:43px;top:170px;width:194px;height:31px;padding:0 12px;font-size:9px">Password
    <svg width="12" height="13" viewBox="0 0 24 24" fill="none" stroke="#222" stroke-width="1.8"><rect x="5" y="10" width="14" height="12" rx="2"/><path d="M8 10V7a4 4 0 0 1 8 0v3"/><circle cx="12" cy="16" r="1.3"/></svg></div>
  <div class="signin" style="left:41px;top:267px;width:194px;height:36px;padding:0 17px;font-size:16px">Sign In
    <svg width="25" height="12" viewBox="0 0 44 20" fill="none" stroke="#fff" stroke-width="2"><path d="M0 10h42M33 2l9 8-9 8"/></svg></div>
  <div class="or-badge" style="left:123px;top:346px;width:32px;height:32px;font-size:8.5px">OR</div>
  <p class="no-account" style="top:403px;font-size:12.5px">Don't have a Pelvorin Account</p>
  <div class="register" style="left:107px;top:443px;width:65px;height:26px;font-size:8.5px">Register</div>
</section>

<!-- dawn planner -->
<section class="screen planner" style="left:85px;top:630px;width:280px;height:498px;background:var(--navy)">
  <header class="app-header"><span class="name">PELVORIN</span>
    <svg width="18" height="18" viewBox="0 0 24 24" fill="none" stroke="#fff" stroke-width="1.5"><circle cx="12" cy="12" r="10.5"/><circle cx="12" cy="10" r="3.8"/><path d="M5 19.5c2-3.2 4.3-4.5 7-4.5s5 1.3 7 4.5"/></svg></header>
  <div class="night-sky" role="img" aria-label="Starry night sky over a dark horizon"></div>
  <svg class="abs" style="left:117px;top:52px" width="46" height="28" viewBox="0 0 46 28" fill="none" stroke="var(--orange)" stroke-width="2" stroke-linecap="round">
    <path d="M13 18a10 10 0 0 1 20 0"/><path d="M23 1v4M12 5l2.5 3M34 5l-2.5 3M5 12l4 2M41 12l-4 2"/><path d="M2 19h42M7 23h32M13 27h20"/></svg>
  <div class="section-label" style="top:94px">SELECT DATE</div>
  <div class="select" style="left:24px;top:123px;width:66px">25 <svg width="12" height="7" viewBox="0 0 14 8" fill="none" stroke="#111" stroke-width="1.4"><path d="M1 1l6 6 6-6"/></svg></div>
  <div class="select" style="left:105px;top:123px;width:67px">MAY <svg width="12" height="7" viewBox="0 0 14 8" fill="none" stroke="#111" stroke-width="1.4"><path d="M1 1l6 6 6-6"/></svg></div>
  <div class="select" style="left:186px;top:123px;width:67px">2024 <svg width="12" height="7" viewBox="0 0 14 8" fill="none" stroke="#111" stroke-width="1.4"><path d="M1 1l6 6 6-6"/></svg></div>
  <div class="section-label" style="top:181px">LOCATION</div>
  <div class="select" style="left:24px;top:210px;width:228px;font-size:8.5px;letter-spacing:.04em;padding:0 14px 0 13px">
    <span style="display:flex;align-items:center;gap:9px"><svg width="9" height="12" viewBox="0 0 18 24"><path d="M9 0a8 8 0 0 1 8 8c0 6-8 16-8 16S1 14 1 8a8 8 0 0 1 8-8z" fill="#4a2466"/><circle cx="9" cy="8" r="3" fill="#fff"/></svg>SELECT LOCATION</span>
    <svg width="13" height="8" viewBox="0 0 14 8" fill="none" stroke="#111" stroke-width="1.4"><path d="M1 1l6 6 6-6"/></svg></div>
  <svg class="abs" style="left:0;top:265px" width="280" height="80" viewBox="0 0 280 80">
    <defs><path id="dawn-arc" d="M45 53 Q140 -2 235 53"/></defs>
    <path d="M0 65 Q140 0 280 65 V80 H0z" fill="var(--navy)"/>
    <text font-family="Roboto, sans-serif" font-size="14" font-weight="500" fill="#fff" letter-spacing="3"><textPath href="#dawn-arc" startOffset="50%" text-anchor="middle">ASTRONOMICAL DAWN</textPath></text>
  </svg>
  <div class="time-pill" style="top:336px"><span class="label">
    <svg width="24" height="13" viewBox="0 0 24 13" fill="none" stroke-linecap="round"><path d="M6 11a6 6 0 0 1 12 0z" fill="#f3b21c"/><path d="M12 1v2M5 3l1.3 1.6M19 3l-1.3 1.6M1 8h2M21 8h2" stroke="#f3b21c" stroke-width="1.2"/><path d="M1 12h22" stroke="#9ab" stroke-width="1"/></svg>START AT</span><span class="value">6:46 AM</span></div>
  <div class="time-pill" style="top:387px"><span class="label">
    <svg width="24" height="16" viewBox="0 0 24 16" fill="none" stroke-linecap="round"><circle cx="12" cy="9" r="5" fill="#f3c31c"/><path d="M12 0v2M5 2l1.3 1.6M19 2l-1.3 1.6M1 8h3M20 8h3" stroke="#f3b21c" stroke-width="1.2"/><path d="M3 14h18M7 16h10" stroke="#9ab" stroke-width="1"/></svg>ENDS AT</span><span class="value">7:46 AM</span></div>
  <div class="reminder-bar">
    <svg width="22" height="24" viewBox="0 0 22 24" fill="none" stroke="#fff" stroke-width="1.4" stroke-linecap="round"><path d="M4 18V11a7 7 0 0 1 14 0v7l2 2H2z"/><path d="M8.5 21a2.5 2.5 0 0 0 5 0"/><path d="M2 7a10 10 0 0 1 3-4M20 7a10 10 0 0 0-3-4"/></svg>
    SET REMINDER</div>
</section>

<!-- sunrise countdown -->
<section class="screen countdown" style="left:411px;top:627px;width:281px;height:499px">
  <div class="sunrise-scene" role="img" aria-label="Photograph of the sun rising over a dark hilly horizon with a golden sky"></div>
  <header class="app-header"><span class="name">PELVORIN</span>
    <svg width="18" height="18" viewBox="0 0 24 24" fill="none" stroke="#fff" stroke-width="1.5"><circle cx="12" cy="12" r="10.5"/><circle cx="12" cy="10" r="3.8"/><path d="M5 19.5c2-3.2 4.3-4.5 7-4.5s5 1.3 7 4.5"/></svg></header>
  <div class="greeting">Hi User</div>
  <h2 class="headline">ASTRONOMICAL<br>DAWN HAS STARTED</h2>
  <div class="flip" style="left:45px"><span>0</span><span>2</span></div>
  <div class="flip" style="left:113px"><span>1</span><span>9</span></div>
  <div class="flip" style="left:181px"><span>2</span><span>1</span></div>
  <div class="unit" style="left:46px">HOURS</div>
  <div class="unit" style="left:109px">MINUTES</div>
  <div class="unit" style="left:177px">SECONDS</div>
</section>

</body>
</html>
```